Property management company looking for modern card design

We at Blue Maple Holdings provides property management services for its residential and commercial properties, with expertise in all categories of multifamily, industrial and office projects throughout California.

We need a business card design that is professional and modern designed business card. In our field, clients get hundreds of business cards, we would like our card to stand out.

Please avoid small print.

Target Market(s)

Professionals and high end clients

Industry/Entity Type

Financial Planning

Contact Information for Business Card

Company Name: Blue Maple Holdings, Name, email, license #, phone number, website bluemapleholdings.example

Font styles to use
Sans Serif

Requirements
Must have
• The card design needs to be adaptable because there is a possibly we will be expanding into different sectors other than real estate. The card design should be focused on financial planning and asset management.
Nice to have
• Modern and simple business card. Eye catching. Non-standard size/shaped cards would be great.
• bluemapleholdings.example
Should not have
• Too many bright color or any pictures or shapes of real estate stuff.

```html
<!DOCTYPE html>
<html lang="en">
<head>
<meta charset="utf-8">
<title>Blue Maple Holdings – Business Card</title>
<link href="https://fonts.googleapis.com/css2?family=Montserrat:wght@300;400&display=swap" rel="stylesheet">
<style>
  :root {
    --page-bg: #3a3739;
    --front-bg: #0d120e;
    --back-bg: #1f4a27;
    --brand-green: #3fae49;
    --line-silver: #d9e1d9;
  }
  * { margin: 0; padding: 0; box-sizing: border-box; }
  html, body {
    width: 1200px;
    height: 1000px;
    overflow: hidden;
    background: var(--page-bg);
    font-family: "Montserrat", Arial, sans-serif;
  }
  .sheet {
    width: 1200px;
    height: 1000px;
    display: flex;
    flex-direction: column;
    align-items: center;
    justify-content: center;
    gap: 60px;
  }
  .card {
    position: relative;
    width: 700px;
    height: 400px;
    box-shadow: 0 14px 30px rgba(0, 0, 0, 0.35);
  }
  .card-front {
    background: var(--front-bg);
    display: flex;
    align-items: center;
    justify-content: center;
  }
  .brand-name {
    color: var(--brand-green);
    font-weight: 400;
    font-size: 40px;
    letter-spacing: 1px;
  }
  .card-back {
    background: var(--back-bg);
    color: var(--line-silver);
    font-weight: 300;
  }
  .contact-table {
    position: absolute;
    left: 50px;
    top: 110px;
    width: 600px;
    height: 150px;
    border: 1.5px solid var(--line-silver);
    display: grid;
    grid-template-rows: 62px 1fr;
  }
  .holder-name {
    display: flex;
    align-items: center;
    justify-content: center;
    border-bottom: 1.5px solid var(--line-silver);
    font-size: 17px;
    letter-spacing: 2px;
    text-transform: uppercase;
  }
  .contact-row {
    display: grid;
    grid-template-columns: 150px 1fr 222px;
  }
  .contact-cell {
    display: flex;
    align-items: center;
    justify-content: center;
    padding: 0 10px;
    font-size: 17px;
    white-space: nowrap;
    overflow: hidden;
  }
  .contact-cell + .contact-cell { border-left: 1.5px solid var(--line-silver); }
  .contact-phone { font-size: 20px; }
  .contact-web { font-size: 14px; }
  .license-number {
    position: absolute;
    right: 50px;
    top: 274px;
    font-size: 14px;
    letter-spacing: 0.5px;
  }
</style>
</head>
<body>
  <main class="sheet">
    <section class="card card-front" aria-label="Card front">
      <h1 class="brand-name">Blue Maple Holdings</h1>
    </section>

    <section class="card card-back" aria-label="Card back">
      <div class="contact-table">
        <div class="holder-name">Your Name Here</div>
        <div class="contact-row">
          <div class="contact-cell contact-phone">+123456789</div>
          <div class="contact-cell contact-email">admin@youremail.com</div>
          <div class="contact-cell contact-web">bluemapleholdings.example</div>
        </div>
      </div>
      <p class="license-number"># 1234568</p>
    </section>
  </main>
</body>
</html>
```